Graphic- Educational Visual

Tandem Dog Training has created an educational tool to help its students understand and prioritize some key concepts in their dog training.

We are requesting a visual of this tool be designed.

Name/title of tool (to be included in graphic): The Tandem Compass
Description: Funnel (inverted pyramid).

From top to bottom, the levels are called:

Connect
Develop
Progress
Refine

The diagram should also include a cycle around it to, to represent that one is always moving through the levels.

Business colours are included below to make sure the funnel's colours complement the website colours or at least don't clash:

#0AA1C7 Blue and #7FC31B Green
Purple as a secondary colour -75279C

For reference, business logo is attached.

```html
<!DOCTYPE html>
<html lang="en">
<head>
<meta charset="UTF-8">
<title>The Tandem Compass – Tandem Dog Training</title>
<link href="https://fonts.googleapis.com/css2?family=Fredoka:wght@600&family=Kaushan+Script&display=swap" rel="stylesheet">
<style>
  :root {
    --brand-blue: #0AA1C7;
    --brand-green: #7FC31B;
    --brand-purple: #75279C;
    --band-blue: #1a9fd0;
    --band-green: #17c41d;
    --band-purple: #9a1fa6;
    --tier-connect: #9a0a74;
    --tier-develop: #9c6bc6;
    --tier-progress: #3d98d6;
    --tier-refine: #86d34c;
    --tier-edge: #4a1f5e;
    --white: #ffffff;
    --page: #ffffff;
  }
  * { margin: 0; padding: 0; box-sizing: border-box; }
  html, body { width: 1200px; height: 1000px; overflow: hidden; background: var(--page); }
  .canvas { position: relative; width: 1200px; height: 1000px; overflow: hidden; background: var(--page); }

  .poster { position: absolute; left: 238px; top: 50px; width: 800px; height: 870px; overflow: hidden; }

  .color-bands { position: absolute; top: 0; left: 0; width: 800px; height: 12px; }
  .color-bands span { position: absolute; top: 0; height: 12px; }
  .band-blue { left: 0; width: 228px; background: var(--band-blue); }
  .band-green { left: 248px; width: 270px; background: var(--band-green); }
  .band-purple { left: 534px; width: 266px; background: var(--band-purple); }

  .scene-photo {
    position: absolute; top: 12px; left: 0; width: 800px; height: 858px;
    background:
      radial-gradient(ellipse at 80% 60%, rgba(230,230,230,0.25), transparent 30%),
      radial-gradient(ellipse at 15% 55%, #8c8f6e 0%, transparent 55%),
      linear-gradient(180deg, #1e3524 0%, #2d4a31 40%, #4f6a3e 75%, #3e5e33 100%);
  }
  .dashed-rule { position: absolute; top: 24px; left: 0; width: 800px; border-top: 2px dashed rgba(80,160,150,0.6); }

  .title { position: absolute; top: 60px; left: 0; width: 800px; height: 160px; color: var(--white); }
  .title-the {
    position: absolute; left: 80px; top: 30px;
    font-family: "Kaushan Script", cursive; font-size: 84px; line-height: 1;
    transform: rotate(-6deg);
  }
  .title-word {
    position: absolute; font-family: "Fredoka", sans-serif; font-weight: 600;
    line-height: 1; letter-spacing: 1px; text-shadow: 0 2px 4px rgba(0,0,0,0.35);
  }
  .title-line1 { left: 258px; top: 2px; font-size: 76px; }
  .title-line2 { left: 258px; top: 76px; font-size: 76px; }

  .diagram { position: absolute; left: 0; top: 0; width: 800px; height: 870px; }
  .tier-label {
    font-family: "Fredoka", sans-serif; font-weight: 600; fill: var(--white);
    text-anchor: middle; letter-spacing: 1px;
  }

  .brand-name {
    position: absolute; left: 0; top: 752px; width: 800px; text-align: center;
    font-family: "Fredoka", sans-serif; font-weight: 600; font-size: 50px;
    color: var(--brand-blue); line-height: 1;
  }
</style>
</head>
<body>
<div class="canvas">
  <section class="poster">
    <div class="scene-photo" role="img" aria-label="Photo of a black and white border collie running towards the camera through long grass in a wooded field"></div>
    <div class="color-bands"><span class="band-blue"></span><span class="band-green"></span><span class="band-purple"></span></div>
    <div class="dashed-rule"></div>

    <h1 class="title">
      <span class="title-the">The</span>
      <span class="title-word title-line1">TANDEM</span>
      <span class="title-word title-line2">COMPASS</span>
    </h1>

    <svg class="diagram" viewBox="0 0 800 870" width="800" height="870">
      <defs>
        <linearGradient id="g-connect" x1="0" y1="0" x2="0" y2="1"><stop offset="0" stop-color="#a8107f"/><stop offset="1" stop-color="var(--tier-connect)"/></linearGradient>
        <linearGradient id="g-develop" x1="0" y1="0" x2="0" y2="1"><stop offset="0" stop-color="#a579cf"/><stop offset="1" stop-color="#8c58b8"/></linearGradient>
        <linearGradient id="g-progress" x1="0" y1="0" x2="0" y2="1"><stop offset="0" stop-color="#47a3e0"/><stop offset="1" stop-color="#2f86c4"/></linearGradient>
        <linearGradient id="g-refine" x1="0" y1="0" x2="0" y2="1"><stop offset="0" stop-color="#8fdc55"/><stop offset="1" stop-color="#6fc33a"/></linearGradient>
        <linearGradient id="g-cycle-in" x1="0" y1="0" x2="0" y2="1"><stop offset="0" stop-color="#1a7fc4" stop-opacity="0.2"/><stop offset="1" stop-color="#1a7fc4"/></linearGradient>
        <linearGradient id="g-cycle-out" x1="0" y1="1" x2="0" y2="0"><stop offset="0" stop-color="#3aa6d8" stop-opacity="0.1"/><stop offset="1" stop-color="#8fd0ea" stop-opacity="0.8"/></linearGradient>
      </defs>

      <!-- cycle arrows -->
      <path class="cycle-down" d="M62 330 C40 470 90 580 170 612" fill="none" stroke="url(#g-cycle-in)" stroke-width="16"/>
      <polygon class="cycle-down-head" points="150,580 205,625 145,640" fill="#1a7fc4"/>
      <path class="cycle-up" d="M480 600 C640 590 710 520 712 410" fill="none" stroke="url(#g-cycle-out)" stroke-width="14"/>
      <polygon class="cycle-up-head" points="688,415 712,330 748,410" fill="#9fd6ec" opacity="0.85"/>

      <!-- funnel tiers -->
      <polygon class="tier-connect" points="95,257 692,257 652,338 134,338" fill="url(#g-connect)"/>
      <polygon class="tier-edge" points="134,338 652,338 640,357 142,357" fill="var(--tier-edge)"/>
      <text class="tier-label" x="382" y="315" font-size="44">CONNECT</text>

      <polygon class="tier-develop" points="142,357 640,357 614,440 174,440" fill="url(#g-develop)"/>
      <polygon class="tier-edge" points="174,440 614,440 600,457 202,457" fill="#5a2a78"/>
      <text class="tier-label" x="392" y="416" font-size="44">DEVELOP</text>

      <polygon class="tier-progress" points="202,457 567,457 532,548 234,548" fill="url(#g-progress)"/>
      <polygon class="tier-edge" points="234,548 532,548 520,565 267,565" fill="#3a2f7a"/>
      <text class="tier-label" x="380" y="520" font-size="44">PROGRESS</text>

      <polygon class="tier-refine" points="267,565 482,565 442,652 317,652" fill="url(#g-refine)"/>
      <text class="tier-label" x="374" y="622" font-size="40">REFINE</text>
    </svg>

    <p class="brand-name">Tandem Dog Training</p>
  </section>
</div>
</body>
</html>
```